Child care/Preparatory Business Card Design & logo design

I need a logo to use on a business card, letterhead, uniform and promotional material for a new business called 'Kestrel Ridge Preparatory'. It is located in the north west of Western Australia in the Pilbara region. The service will provide a 'Preparation for Education' program for 3 and 4 year old children. I would like a logo that shows unity, or belonging in children. I like the colour blue, any primary colours would be suitable. The design needs to be cheerful and appealing to children whilst still having an 'elite' edge to it.

Target Market(s)

Families with young children

Industry/Entity Type

Business

Contact Information for Business Card

Marcia Hollis Director
Kestrel Ridge Preparatory
M 0491 570 318
office@kestrelridgeprep.com.au
PO Box 581 Tarrent WA 6731

Preparation for Education

```html
<!DOCTYPE html>
<html lang="en">
<head>
<meta charset="utf-8">
<title>Kestrel Ridge Preparatory – Business Card</title>
<link rel="stylesheet" href="https://fonts.googleapis.com/css2?family=Architects+Daughter&family=Josefin+Sans:wght@300;400&display=swap">
<style>
  :root {
    --backdrop: #d9d9d9;
    --card: #ffffff;
    --sky: #5cc3ea;
    --sky-soft: #8fd3ee;
    --orange: #f39321;
    --shadow: rgba(0, 0, 0, 0.18);
  }
  * { box-sizing: border-box; margin: 0; padding: 0; }
  html, body {
    width: 1200px;
    height: 900px;
    overflow: hidden;
    background: var(--backdrop);
  }
  .stage {
    position: relative;
    width: 1200px;
    height: 900px;
  }
  .card {
    position: absolute;
    left: 100px;
    top: 164px;
    width: 1000px;
    height: 572px;
    background: var(--card);
    box-shadow: 0 10px 30px var(--shadow);
  }
  .brand-mark {
    position: absolute;
    left: 130px;
    top: 110px;
    width: 140px;
    height: 140px;
    border-radius: 50%;
    background: var(--sky);
  }
  .brand {
    position: absolute;
    left: 300px;
    top: 128px;
  }
  .brand-name {
    font-family: "Architects Daughter", cursive;
    font-size: 44px;
    letter-spacing: 2px;
    color: var(--sky);
    text-transform: uppercase;
    line-height: 1.1;
  }
  .brand-tagline {
    margin-top: 4px;
    margin-left: 44px;
    font-family: "Architects Daughter", cursive;
    font-size: 27px;
    letter-spacing: 1.5px;
    color: var(--orange);
    text-transform: uppercase;
  }
  .person {
    position: absolute;
    left: 80px;
    top: 406px;
  }
  .person-name {
    font-family: "Josefin Sans", sans-serif;
    font-weight: 300;
    font-size: 38px;
    letter-spacing: 3px;
    color: var(--sky);
  }
  .person-role {
    margin-top: 6px;
    font-family: "Josefin Sans", sans-serif;
    font-weight: 400;
    font-size: 20px;
    letter-spacing: 2px;
    color: var(--orange);
  }
  .contact {
    position: absolute;
    left: 420px;
    top: 360px;
    list-style: none;
    font-family: "Josefin Sans", sans-serif;
    font-weight: 300;
    font-size: 22px;
    letter-spacing: 1px;
    color: var(--sky-soft);
  }
  .contact li {
    display: flex;
    align-items: center;
    gap: 10px;
    height: 34px;
  }
  .contact-icon {
    width: 20px;
    height: 20px;
    fill: var(--sky);
    flex: none;
  }
  .contact-label { color: var(--sky); }
</style>
</head>
<body>
  <main class="stage">
    <section class="card">
      <div class="brand-mark"></div>
      <header class="brand">
        <h1 class="brand-name">Kestrel Ridge Preparatory</h1>
        <p class="brand-tagline">Preparing for Education</p>
      </header>

      <div class="person">
        <p class="person-name">Marcia Hollis</p>
        <p class="person-role">Director</p>
      </div>

      <ul class="contact">
        <li>
          <svg class="contact-icon" viewBox="0 0 20 20" aria-hidden="true"><rect x="5" y="1" width="10" height="18" rx="2"/><rect x="7" y="4" width="6" height="9" fill="#fff"/></svg>
          <span><span class="contact-label">mobile:</span> 0491 570 318</span>
        </li>
        <li>
          <svg class="contact-icon" viewBox="0 0 20 20" aria-hidden="true"><rect x="1" y="4" width="18" height="12" rx="1"/><path d="M2 5 L10 11 L18 5" fill="none" stroke="#fff" stroke-width="1.6"/></svg>
          <span><span class="contact-label">email:</span> office@kestrelridgeprep.com.au</span>
        </li>
        <li>
          <svg class="contact-icon" viewBox="0 0 20 20" aria-hidden="true"><path d="M10 2 L19 10 H16 V18 H12 V13 H8 V18 H4 V10 H1 Z"/></svg>
          <span>PO Box 581 Tarrent, WA, 6731.</span>
        </li>
      </ul>
    </section>
  </main>
</body>
</html>
```